Entrepreneurial Book Cover -

I need both an eBook cover and a physical book cover with back matter (6in by 9in) for my new book on using content to build a personal brand. I would like a clean cover like the one for Russell Tabor's Forging Your Quiet Compass or Colette Faraday's Lighthouse. I want the cover to communicate the content creation process. Book Title - Posts Which Glow Then Gather. Subtitle: Create content that helps you build a magnetic and profitable personal brand. Author: Philippa Okwuosa

```html
<!DOCTYPE html>
<html lang="en">
<head>
<meta charset="utf-8">
<title>Posts Which Glow Then Gather – Book Cover</title>
<link href="https://fonts.googleapis.com/css2?family=Lato:wght@400;700;900&family=Playfair+Display:wght@700;900&display=swap" rel="stylesheet">
<style>
  :root {
    --cream: #f3f4e2;
    --mist: #a8c2c6;
    --red: #e4201a;
    --title-red: #ee3a3a;
    --ink: #5a5a5a;
    --spine: #6f6f6f;
    --white: #ffffff;
  }
  * { margin: 0; padding: 0; box-sizing: border-box; }
  html, body { width: 1200px; height: 857px; overflow: hidden; }
  body { font-family: "Lato", sans-serif; }
  .cover {
    position: relative;
    width: 1200px;
    height: 857px;
    overflow: hidden;
    background: var(--cream);
  }
  .panel {
    position: absolute;
    top: 0;
    height: 857px;
    background: radial-gradient(ellipse at 50% 48%, var(--cream) 35%, #e3eada 65%, var(--mist) 115%);
  }
  .back { left: 0; width: 573px; }
  .front { left: 625px; width: 575px; }
  .spine {
    position: absolute;
    left: 573px; top: 0;
    width: 52px; height: 857px;
    background: var(--spine);
  }
  .band {
    position: absolute;
    top: 773px;
    height: 59px;
    background: var(--red);
  }
  .back .band { left: 0; width: 573px; }
  .front .band {
    left: 0; width: 575px;
    display: flex; align-items: center; justify-content: center;
  }
  .author-front {
    color: var(--white);
    font-weight: 700;
    font-size: 28px;
    letter-spacing: 3px;
    word-spacing: 8px;
    padding-left: 8px;
  }
  .back-title {
    position: absolute;
    top: 146px; left: 0; width: 573px;
    text-align: center;
    color: var(--red);
    font-weight: 900;
    font-size: 24px;
    letter-spacing: 0.2px;
  }
  .blurb {
    position: absolute;
    top: 244px; left: 75px; width: 424px;
    text-align: center;
    color: var(--ink);
    font-size: 15.5px;
    line-height: 19.1px;
  }
  .barcode-box {
    position: absolute;
    left: 357px; top: 722px;
    width: 191px; height: 114px;
    background: var(--white);
    box-shadow: 0 2px 6px rgba(0,0,0,0.35);
  }
  .spine-text {
    position: absolute;
    left: 599px;
    color: var(--white);
    font-weight: 900;
    font-size: 18px;
    letter-spacing: 1.5px;
    white-space: nowrap;
    transform-origin: 0 0;
    transform: rotate(90deg) translateY(-50%);
  }
  .spine-title { top: 38px; }
  .spine-author { top: 588px; }
  .subtitle {
    position: absolute;
    top: 28px; left: 0; width: 575px;
    text-align: center;
    color: var(--ink);
    font-size: 21px;
    line-height: 27px;
  }
  .title-art {
    position: absolute;
    left: 0; top: 96px;
    width: 575px; height: 330px;
  }
  .title-big { font-family: "Playfair Display", serif; font-weight: 900; fill: var(--title-red); }
  .title-small { font-family: "Playfair Display", serif; font-weight: 700; fill: var(--ink); }
  .rule { stroke: var(--red); stroke-width: 3; }
  .illustration {
    position: absolute;
    left: 91px; top: 432px;
    width: 310px; height: 316px;
    background: linear-gradient(160deg, rgba(90,58,110,0.35) 0%, rgba(238,70,70,0.55) 60%, rgba(238,70,70,0.15) 100%);
    border-radius: 40% 30% 45% 35%;
  }
</style>
</head>
<body>
<div class="cover">
  <section class="panel back">
    <h2 class="back-title">POSTS WHICH GLOW THEN GATHER</h2>
    <p class="blurb">Lorem ipsum dolor sit amet, consectetur adipisci elit, sed eiusmod tempor incidunt ut labore et dolore magna aliqua. Ut enim ad minim veniam, quis nostrum exercitationem ullam corporis suscipit laboriosam, nisi ut aliquid ex ea commodi consequatur. Quis aute iure reprehenderit in voluptate velit esse cillum dolore eu fugiat nulla pariatur. Excepteur sint obcaecat cupiditat non proident, sunt in culpa qui officia deserunt mollit anim id est laborum.<br>Lorem ipsum dolor sit amet, consectetur adipisci elit, sed eiusmod tempor incidunt ut labore et dolore magna aliqua. Ut enim ad minim veniam, quis nostrum exercitationem ullam corporis suscipit laboriosam, nisi ut aliquid ex ea commodi consequatur. Quis aute iure reprehenderit in voluptate velit esse cillum dolore eu fugiat nulla pariatur. Excepteur sint obcaecat cupiditat non proident, sunt in culpa qui officia deserunt mollit anim id est laborum</p>
    <div class="band"></div>
    <div class="barcode-box"></div>
  </section>

  <div class="spine"></div>
  <span class="spine-text spine-title">POSTS WHICH GLOW THEN GATHER</span>
  <span class="spine-text spine-author">PHILIPPA OKWUOSA</span>

  <section class="panel front">
    <p class="subtitle">Create content that helps you build<br>a magnetic and profitable personal brand</p>
    <svg class="title-art" viewBox="0 0 575 330" aria-label="Posts Which Glow Then Gather">
      <text class="title-big" x="99" y="60" font-size="72" textLength="372" lengthAdjust="spacingAndGlyphs">POSTS</text>
      <line class="rule" x1="47" y1="87" x2="181" y2="87"/>
      <line class="rule" x1="385" y1="87" x2="519" y2="87"/>
      <text class="title-small" x="283" y="98" font-size="38" text-anchor="middle">WHICH</text>
      <text class="title-big" x="99" y="180" font-size="94" textLength="372" lengthAdjust="spacingAndGlyphs">GLOW</text>
      <line class="rule" x1="47" y1="209" x2="181" y2="209"/>
      <line class="rule" x1="385" y1="209" x2="519" y2="209"/>
      <text class="title-small" x="283" y="219" font-size="38" text-anchor="middle">THEN</text>
      <text class="title-big" x="99" y="320" font-size="116" textLength="372" lengthAdjust="spacingAndGlyphs">GATHER</text>
    </svg>
    <div class="illustration" role="img" aria-label="Illustration of a woman with a megaphone riding a red paper plane"></div>
    <div class="band"><span class="author-front">PHILIPPA OKWUOSA</span></div>
  </section>
</div>
</body>
</html>
```